Blog Header Design + 2 Buttons + Colortheme

Hello,
I am looking for a fresh and catchy design for this blog project.
It can have a simplistic touch but I am open to all ideas which fit to the concept.
Please have a look at the pictures I've uploaded.
The website is called
http://www.wtwhn-blog.net
it is a blog which presents weird or extraordinary products. The URL is short for the german phrase "Was Toll Wäre Hier Nun?" it means "How cool is that?". Where "Geil" has the meaning of "Cool".
So yea, that is basically the idea of what it should stand for.
What I need is:
- a colortheme for the website
- a logo or banner at the top of the homesite (see the picture of the text I uploaded, if you could write it in this kind of deign that would look nice I guess)
- buttons for the product elements of the homesite and on the productdetail pages ("Geil!" Button and Price Button/Sign)
- background design (can fit the design idea but shouldnt be too distracting)
- if it is needed by or serves the design, the menu can be changed as well, but it can also stay as it is
optional for a complete set is needed:
- a favicon that fits the theme
- a facebook cover and profile picture
If you have any further questions please let know and I will respond to you as soon as possible.
Again, I am open to ALL design ideas for the whole website concept and would be glad to find a long term deign partner for other projects as well. THANK YOU!

```html
<!DOCTYPE html>
<html lang="de">
<head>
<meta charset="utf-8">
<title>Was Toll Wäre Hier Nun?</title>
<link href="https://fonts.googleapis.com/css2?family=Arimo:wght@400;700&display=swap" rel="stylesheet">
<style>
:root{
  --blue:#1a8cc4;
  --blue-dark:#0f78ad;
  --sky:#bfe4f6;
  --sky-soft:#e3f4fc;
  --text:#444;
  --text-soft:#5a5a5a;
  --line:#dcdcdc;
  --white:#fff;
}
*{box-sizing:border-box;margin:0;padding:0}
html,body{width:1200px;height:983px;overflow:hidden}
body{font-family:"Arimo",Arial,sans-serif;background:var(--white);position:relative;color:var(--text)}
.page-backdrop{position:absolute;inset:0;background:linear-gradient(180deg,#8fd0ee 0,#d6effa 70px,#fff 130px)}
.side-pattern{position:absolute;top:0;bottom:31px;width:230px;background:linear-gradient(180deg,rgba(191,228,246,.55),rgba(191,228,246,.35))}
.side-pattern.left{left:0}
.side-pattern.right{right:0}

.brand{position:absolute;left:228px;top:12px;width:148px;height:86px;display:flex;align-items:center;gap:8px}
.brand-square{width:18px;height:18px;background:var(--blue);flex:none}
.brand-name{font-weight:700;font-size:17px;line-height:1.15;color:var(--blue);text-transform:uppercase}

.cart{position:absolute;left:848px;top:4px;display:flex;gap:6px}
.cart-info{display:flex;flex-direction:column;align-items:flex-start}
.cart-count{font-size:10px;color:var(--blue-dark);line-height:13px;white-space:nowrap}
.checkout{display:block;margin-top:2px;width:72px;height:16px;background:var(--blue);color:#fff;font-size:10px;line-height:16px;text-align:center}

.main-nav{position:absolute;left:380px;top:40px;width:588px;height:30px;background:var(--white);display:flex;align-items:center;padding-left:30px;white-space:nowrap}
.main-nav a{font-size:11px;color:var(--blue);text-decoration:none;padding:0 8px;height:30px;line-height:30px;white-space:nowrap;flex:none}
.main-nav a.active{color:var(--text);border-top:2px solid var(--blue);line-height:26px;background:#fff}

.toolbar{position:absolute;left:380px;top:74px;width:475px;height:28px;background:var(--blue);display:flex;align-items:center;padding-left:10px;gap:10px}
.toolbar svg{flex:none}
.search{margin-left:12px;width:340px;height:20px;background:#fff;border:1px solid #d6d6d6;display:flex;align-items:center;justify-content:space-between;padding:0 6px;font-size:9px;color:#999}
.share{position:absolute;left:855px;top:74px;display:flex;gap:2px}
.share span{width:24px;height:28px;background:var(--blue-dark)}

.products{position:absolute;left:239px;top:107px;display:grid;grid-template-columns:repeat(3,232px);column-gap:13px;row-gap:14px}
.product{width:232px;height:265px;background:#fff;border:1px solid var(--line);padding:6px;position:relative;overflow:hidden}
.product-photo{width:220px;height:165px;position:relative}
.price-tag{position:absolute;right:0;bottom:0;display:flex;height:25px;color:#fff;font-weight:700;font-size:14px;line-height:25px}
.price-tag .geil{background:var(--blue);padding:0 6px;border-right:1px solid #fff}
.price-tag .price{background:var(--blue-dark);padding:0 6px}
.product h2{font-weight:400;font-size:16px;line-height:19px;color:var(--text);margin:12px 0 0 0;white-space:nowrap}
.product p{font-size:9px;line-height:14px;color:var(--text-soft);margin-top:9px;width:216px;height:42px;overflow:hidden}
.more{position:absolute;right:13px;bottom:7px;width:40px;height:13px;background:var(--blue);color:#fff;font-size:9px;line-height:13px;text-align:center;text-decoration:none}

.site-footer{position:absolute;left:0;bottom:0;width:1200px;height:31px;background:var(--sky-soft);border-top:1px solid #cbe9f7;text-align:center;font-size:10px;line-height:30px;color:#666}
</style>
</head>
<body>
<div class="page-backdrop"></div>
<div class="side-pattern left" role="img" aria-label="Streumuster aus hellblauen Einkaufstüten"></div>
<div class="side-pattern right" role="img" aria-label="Streumuster aus hellblauen Einkaufstüten"></div>

<header>
  <div class="brand"><span class="brand-square"></span><span class="brand-name">Was Toll Wäre Hier Nun?</span></div>

  <div class="cart">
    <svg width="36" height="26" viewBox="0 0 36 26" aria-hidden="true"><path d="M1 3h6l4 14h18l4-11H9" fill="none" stroke="#1a8cc4" stroke-width="3"/><circle cx="13" cy="22" r="2.5" fill="#1a8cc4"/><circle cx="27" cy="22" r="2.5" fill="#1a8cc4"/></svg>
    <div class="cart-info"><span class="cart-count">0 Item in you cart</span><a class="checkout">Checkout ›</a></div>
  </div>

  <nav class="main-nav">
    <a class="active">Home</a><a>Technik</a><a>Spiel &amp; Spaß</a><a>Kleidung &amp; Accessoires</a><a>Haus &amp; Büro</a><a>Essen &amp; Trinken</a><a>Sonstiges</a>
  </nav>

  <div class="toolbar">
    <svg width="14" height="14" viewBox="0 0 14 14" aria-label="Kalender"><rect x="1" y="2" width="12" height="11" fill="none" stroke="#a9dcf3" stroke-width="1.5"/><path d="M1 5h12M4 1v3M10 1v3" stroke="#a9dcf3" stroke-width="1.5"/></svg>
    <svg width="14" height="14" viewBox="0 0 14 14" aria-label="Favoriten"><path d="M7 12L2 7a3 3 0 015-4 3 3 0 015 4z" fill="#a9dcf3"/></svg>
    <svg width="14" height="14" viewBox="0 0 14 14" aria-label="Preis"><path d="M11 3a5 5 0 100 8M2 6h7M2 8h7" fill="none" stroke="#a9dcf3" stroke-width="1.5"/></svg>
    <svg width="14" height="14" viewBox="0 0 14 14" aria-label="Absteigend"><path d="M2 5l5 5 5-5" fill="none" stroke="#a9dcf3" stroke-width="2"/></svg>
    <svg width="14" height="14" viewBox="0 0 14 14" aria-label="Aufsteigend"><path d="M2 9l5-5 5 5" fill="none" stroke="#a9dcf3" stroke-width="2"/></svg>
    <div class="search"><span>Search...</span><svg width="10" height="10" viewBox="0 0 10 10" aria-hidden="true"><circle cx="4" cy="4" r="3" fill="none" stroke="#aaa" stroke-width="1.2"/><path d="M6 6l3 3" stroke="#aaa" stroke-width="1.2"/></svg></div>
  </div>
  <div class="share" aria-label="Teilen"><span></span><span></span><span></span><span></span></div>
</header>

<main class="products">
  <article class="product">
    <div class="product-photo" role="img" aria-label="Foto eines Zombie-Gartenzwergs neben einem normalen Zwerg" style="background:linear-gradient(135deg,#3c5a2a,#8a3a30 55%,#cfd3c8)"><div class="price-tag"><span class="geil">GEIL!</span><span class="price">€17,64</span></div></div>
    <h2>Zombie Gartenzwerg</h2>
    <p>Dieser gruselig aussehende Zombie Gartenzwerg wird dafür sorgen, dass alle anderen Gartenzwerge lieber das Weite suchen...</p>
    <a class="more">mehr ›</a>
  </article>
  <article class="product">
    <div class="product-photo" role="img" aria-label="Foto karierter Putz-Hausschuhe mit Wischfransen" style="background:linear-gradient(180deg,#4a5a70,#8c7d7a 45%,#c9c4c0)"><div class="price-tag"><span class="geil">GEIL!</span><span class="price">€13,36</span></div></div>
    <h2>Putz Hausschuhe</h2>
    <p>Mit diesem praktischen Paar Putz- und Polierschuhe wird der Fußboden einfach auf Hochglanz poliert, während man...</p>
    <a class="more">mehr ›</a>
  </article>
  <article class="product">
    <div class="product-photo" role="img" aria-label="Foto eines Kindes mit bunten Strohhalm-Röhren" style="background:linear-gradient(135deg,#d8d6cf,#c9b79a 50%,#6a9a5a)"><div class="price-tag"><span class="geil">GEIL!</span><span class="price">€9,90</span></div></div>
    <h2>Strohhalm Bausatz</h2>
    <p>Die Trinkhalm-Pipeline: Bau dir deine eigenen Röhren-Kreationen! Hoch, runter, um die Ecke, bastel eine endlose Reihe...</p>
    <a class="more">mehr ›</a>
  </article>
  <article class="product">
    <div class="product-photo" role="img" aria-label="Foto von Wäsche an einer Leine mit Fledermaus-Klammern" style="background:linear-gradient(135deg,#2c4a28,#6f9a4a 50%,#c94545)"><div class="price-tag"><span class="geil">GEIL!</span><span class="price">€7,44</span></div></div>
    <h2>Fledermaus Klammern</h2>
    <p>Wenn der Nachbar klingelt und dir mitteilt, dass an deiner Wäscheleine Fledermäuse hängen, haha. Praktische Klammern,...</p>
    <a class="more">mehr ›</a>
  </article>
  <article class="product">
    <div class="product-photo" role="img" aria-label="Foto eines aufblasbaren Riesenglobus" style="background:radial-gradient(circle at 60% 45%,#3f79b8,#2b4f7a 45%,#8a7a6a)"><div class="price-tag"><span class="geil">GEIL!</span><span class="price">€87,34</span></div></div>
    <h2>Riesen Globus</h2>
    <p>Einmal um die ganze Welt und das im Wohnzimmer. Mit diesem Erdball in XXL Format macht es einfach riesig Spaß die Welt...</p>
    <a class="more">mehr ›</a>
  </article>
  <article class="product">
    <div class="product-photo" role="img" aria-label="Foto eines Trinksacks unter dem Shirt auf einer Tribüne" style="background:linear-gradient(135deg,#3a3a40,#24304e 55%,#6a6a6a)"><div class="price-tag"><span class="geil">GEIL!</span><span class="price">€19,90</span></div></div>
    <h2>Bierbauch Trinksack</h2>
    <p>Musstet ihr schonmal am Eingang einer Veranstaltung eure Getränke abgeben? Ja? Nervig, oder? Hey, dann gibt es jetzt...</p>
    <a class="more">mehr ›</a>
  </article>
  <article class="product">
    <div class="product-photo" role="img" aria-label="Foto eines Zelts in Form eines blau-weißen Campingbusses" style="background:linear-gradient(180deg,#2e3b2a,#5fa9bf 45%,#3d6b2e)"><div class="price-tag"><span class="geil">GEIL!</span><span class="price">€375,00</span></div></div>
    <h2>Camper Bus Zelt</h2>
    <p>Das Zelt, das denkt es wäre ein Wohnmobil! Perfekt für diejenigen unter euch, die sich auf Musik-Festivals,...</p>
    <a class="more">mehr ›</a>
  </article>
  <article class="product">
    <div class="product-photo" role="img" aria-label="Foto eines Radfahrers mit Regenschirm-Kuppel" style="background:linear-gradient(180deg,#44502e,#6d7a5a 50%,#9a9a96)"><div class="price-tag"><span class="geil">GEIL!</span><span class="price">€79,00</span></div></div>
    <h2>Regenschirm Kuppel</h2>
    <p>Hände frei, Kopf trocken, lustig dabei aussehen, hier bist du richtig. Modern, Funktionell und sehr einfach nutzbar...</p>
    <a class="more">mehr ›</a>
  </article>
  <article class="product">
    <div class="product-photo" role="img" aria-label="Foto einer Hand mit Stempel über bedrucktem Papier" style="background:linear-gradient(135deg,#d9c4b0,#e8e8ea 40%,#3a5fa8 75%,#cfd2d8)"><div class="price-tag"><span class="geil">GEIL!</span><span class="price">€9,90</span></div></div>
    <h2>Daumen Stempelset</h2>
    <p>Du möchtest gerne auch in der analogen Welt den Dingen deine Meinung aufdrücken? Dann kommt dieses Stempelset gerade...</p>
    <a class="more">mehr ›</a>
  </article>
</main>

<footer class="site-footer">AGB &nbsp;|&nbsp; Impressum</footer>
</body>
</html>
```